Business Postcard to attract business listings on directory

We need a postcard that professionally and excitedly highlights the benefits of getting listed on our local business directory.

Our local business directory combines a Quarterly direct mail piece a LOCAL discount card, which means no coupons for people to remember to use, and the power of an online directory and the benefits of local SEO.

Colorful, Vector/Images and Bold text a must

Target Market(s)

Local business, all industrys that service the public, retail,food, construction,plumbing etc.

Industry/Entity Type

Business Directory

Font styles to use
Other font styles liked:
• Calibri,Verdana

Requirements
Must have
• High Quality Graphics
• Vector Icons
• Vibrant Professional Colors
• Place for my contact details
Nice to have
• Some kind of business guy, Cartoonish maybe flying or "exploding" with new business sales
Should not have
• Excessive Blank Space

```html
<!DOCTYPE html>
<html lang="en">
<head>
<meta charset="utf-8">
<title>Local Business Listing Postcard</title>
<link href="https://fonts.googleapis.com/css2?family=Oswald:wght@400;500&family=Open+Sans:ital,wght@1,400&family=Roboto+Condensed:wght@300;400&display=swap" rel="stylesheet">
<style>
  :root {
    --brand-blue: #34429a;
    --brand-red: #e0001b;
    --ink: #2b2b2b;
    --paper: #f3f2f1;
    --paper-shade: #e6e5e4;
    --stage: #ebebeb;
    --stamp: #cfcfcf;
  }
  html, body {
    margin: 0;
    width: 1200px;
    height: 1200px;
    overflow: hidden;
    background: var(--stage);
  }
  .card {
    position: absolute;
    left: 240px;
    width: 720px;
    height: 557px;
    display: block;
  }
  .card--front { top: 28px; }
  .card--back { top: 615px; }
  .headline { font-family: "Oswald", sans-serif; font-weight: 500; fill: #fff; }
  .intro { font-family: "Open Sans", sans-serif; font-style: italic; font-size: 15.5px; fill: var(--ink); }
  .call { font-family: "Oswald", sans-serif; font-weight: 500; fill: var(--brand-red); }
  .email { font-family: "Oswald", sans-serif; font-weight: 400; fill: var(--ink); }
  .web { font-family: "Open Sans", sans-serif; font-size: 19px; fill: #fff; letter-spacing: 7px; }
  .benefit-label { font-family: "Roboto Condensed", sans-serif; font-weight: 400; font-size: 13px; fill: var(--ink); text-anchor: middle; }
  .icon-ring { fill: #fff; stroke: var(--brand-blue); stroke-width: 3; }
  .icon-glyph { fill: var(--brand-red); }
  .icon-line { fill: none; stroke: var(--brand-red); stroke-width: 3; stroke-linecap: round; stroke-linejoin: round; }
  .icon-letter { font-family: "Roboto Condensed", sans-serif; font-size: 12px; fill: #fff; text-anchor: middle; }
</style>
</head>
<body>

<!-- Front of postcard -->
<svg class="card card--front" viewBox="0 0 718 556" xmlns="http://www.w3.org/2000/svg">
  <defs>
    <linearGradient id="paperFront" x1="0" y1="0" x2="0" y2="1">
      <stop offset="0" stop-color="#f1f0ee"/>
      <stop offset="1" stop-color="#ffffff"/>
    </linearGradient>
    <linearGradient id="deskScene" x1="0" y1="0" x2="0" y2="1">
      <stop offset="0" stop-color="#eeeeee"/>
      <stop offset="0.55" stop-color="#4a3f48"/>
      <stop offset="1" stop-color="#d6b07a"/>
    </linearGradient>
  </defs>
  <rect class="card-paper" width="718" height="556" fill="url(#paperFront)"/>

  <rect class="hero-illustration" x="0" y="28" width="322" height="278" fill="url(#deskScene)"
        role="img" aria-label="Illustration of an office desk with a computer showing charts, floating graphs, folders and a coffee cup"/>

  <g class="title-banner">
    <polygon points="278,55 292,55 320,130 306,130" fill="var(--brand-red)"/>
    <polygon points="290,55 718,55 718,130 318,130" fill="var(--brand-blue)"/>
    <text class="headline" x="506" y="108" font-size="42" text-anchor="middle" textLength="336" lengthAdjust="spacingAndGlyphs">LOCAL BUSINESS LISTING</text>
  </g>

  <g class="intro-copy">
    <text class="intro" x="333" y="181" textLength="346" lengthAdjust="spacing">Get found where YOUR shoppers are searching.</text>
    <text class="intro" x="333" y="202" textLength="346" lengthAdjust="spacing">Shoppers are increasingly turning to the web,</text>
    <text class="intro" x="333" y="224" textLength="346" lengthAdjust="spacing">according to LocalPulse’s 5th Annual Local Search</text>
    <text class="intro" x="333" y="245" textLength="346" lengthAdjust="spacing">Usage Study. Shoppers are SEARCHING locally to</text>
    <text class="intro" x="333" y="266">buy in-store and then deciding to purchase.</text>
  </g>

  <polygon class="divider-band" points="0,307 326,307 352,334 718,334 718,345 346,345 320,318 0,318" fill="var(--brand-red)"/>

  <g class="contact">
    <text class="call" x="42" y="398" font-size="44" textLength="256" lengthAdjust="spacingAndGlyphs">CALL: 987.654.32</text>
    <text class="email" x="44" y="438" font-size="24" textLength="250" lengthAdjust="spacingAndGlyphs">EMAIL: INFO@LOCALFINDS.COM</text>
  </g>

  <polygon class="footer-band-red" points="358,522 718,522 718,556 392,556" fill="var(--brand-red)"/>
  <polygon class="footer-band-blue" points="0,478 318,478 388,556 0,556" fill="var(--brand-blue)"/>
  <text class="web" x="46" y="524">www.localfinds.com</text>

  <g class="feature-badges">
    <circle cx="427" cy="403" r="78" fill="#f4f4f4"/>
    <circle cx="427" cy="403" r="62" fill="#e7e2da" role="img" aria-label="Illustration of a hand holding a shopping bag"/>
    <circle cx="427" cy="403" r="78" fill="none" stroke="var(--brand-blue)" stroke-width="6"/>
    <circle cx="603" cy="403" r="78" fill="#f4f4f4"/>
    <circle cx="603" cy="403" r="62" fill="#ef9a8f" role="img" aria-label="Illustration of a red shopping bag with shopping icons bursting out"/>
    <circle cx="603" cy="403" r="78" fill="none" stroke="var(--brand-blue)" stroke-width="6"/>
  </g>
</svg>

<!-- Back of postcard -->
<svg class="card card--back" viewBox="0 0 718 556" xmlns="http://www.w3.org/2000/svg">
  <defs>
    <linearGradient id="paperBack" x1="0" y1="0" x2="0" y2="1">
      <stop offset="0" stop-color="#ececeb"/>
      <stop offset="1" stop-color="#fafafa"/>
    </linearGradient>
  </defs>
  <rect class="card-paper" width="718" height="556" fill="#fff"/>
  <polygon class="benefits-panel" points="0,0 305,0 427,248 280,520 0,520" fill="url(#paperBack)"/>
  <polyline class="chevron-red" points="310,-2 430,248 283,522" fill="none" stroke="var(--brand-red)" stroke-width="8"/>
  <polyline class="chevron-blue" points="324,-2 444,248 297,522" fill="none" stroke="var(--brand-blue)" stroke-width="8"/>
  <rect class="footer-band" x="0" y="519" width="718" height="37" fill="var(--brand-red)"/>
  <rect class="stamp-box" x="619" y="27" width="64" height="64" fill="var(--stamp)"/>

  <!-- Row 1 -->
  <g class="benefit">
    <circle class="icon-ring" cx="86" cy="75" r="30"/>
    <rect class="icon-glyph" x="66" y="73" width="17" height="9" rx="2"/><rect class="icon-glyph" x="69" y="68" width="11" height="6" rx="2"/>
    <rect class="icon-glyph" x="88" y="73" width="17" height="9" rx="2"/><rect class="icon-glyph" x="91" y="68" width="11" height="6" rx="2"/>
    <text class="benefit-label" x="80" y="134">MORE</text>
    <text class="benefit-label" x="80" y="153">FOOT</text>
    <text class="benefit-label" x="80" y="172">TRAFFIC</text>
  </g>
  <g class="benefit">
    <circle class="icon-ring" cx="183" cy="75" r="30"/>
    <rect class="icon-glyph" x="167" y="65" width="32" height="22" rx="2"/>
    <polyline points="167,66 183,78 199,66" fill="none" stroke="#fff" stroke-width="2"/>
    <text class="benefit-label" x="177" y="134">Quarterly Mailing</text>
    <text class="benefit-label" x="177" y="153">To 10,000 local</text>
    <text class="benefit-label" x="177" y="172">shoppers</text>
  </g>
  <g class="benefit">
    <circle class="icon-ring" cx="289" cy="75" r="30"/>
    <rect x="278" y="60" width="22" height="30" rx="3" fill="none" stroke="var(--brand-red)" stroke-width="4"/>
    <text class="benefit-label" x="282" y="134">Desktop &amp; Mobile</text>
    <text class="benefit-label" x="282" y="153">optimized</text>
    <text class="benefit-label" x="282" y="172">online listing</text>
  </g>

  <!-- Row 2 -->
  <g class="benefit">
    <circle class="icon-ring" cx="86" cy="237" r="30"/>
    <rect x="75" y="222" width="15" height="21" fill="none" stroke="var(--brand-red)" stroke-width="2.5"/>
    <rect x="82" y="229" width="15" height="21" fill="#fff" stroke="var(--brand-red)" stroke-width="2.5"/>
    <text class="benefit-label" x="83" y="298">Show up in</text>
    <text class="benefit-label" x="83" y="317">Search Engine</text>
    <text class="benefit-label" x="83" y="336">Results</text>
  </g>
  <g class="benefit">
    <circle class="icon-ring" cx="183" cy="237" r="30"/>
    <polygon class="icon-glyph" points="174,222 192,222 192,252 183,245 174,252"/>
    <text class="icon-letter" x="183" y="241">S</text>
    <text class="benefit-label" x="185" y="298">List Active</text>
    <text class="benefit-label" x="185" y="317">Coupons</text>
    <text class="benefit-label" x="185" y="336">&amp; Deals</text>
  </g>
  <g class="benefit">
    <circle class="icon-ring" cx="275" cy="237" r="30"/>
    <path class="icon-line" d="M260,244 L272,232 M266,232 L272,232 L272,238 M272,244 L288,228 M281,228 L288,228 L288,235"/>
    <text class="benefit-label" x="279" y="298">Connect</text>
    <text class="benefit-label" x="279" y="317">Direct With</text>
    <text class="benefit-label" x="279" y="336">Shoppers</text>
  </g>

  <!-- Row 3 -->
  <g class="benefit">
    <circle class="icon-ring" cx="91" cy="388" r="30"/>
    <polygon class="icon-glyph" points="82,373 100,373 100,403 91,396 82,403"/>
    <text class="icon-letter" x="91" y="392">S</text>
    <text class="benefit-label" x="91" y="444">Support Local</text>
    <text class="benefit-label" x="91" y="463">Shoppers with the</text>
    <text class="benefit-label" x="91" y="482">LOCAL Discount Card</text>
  </g>
  <g class="benefit">
    <circle class="icon-ring" cx="200" cy="388" r="30"/>
    <circle cx="196" cy="392" r="10" fill="none" stroke="var(--brand-red)" stroke-width="5" stroke-dasharray="4 3"/>
    <circle cx="207" cy="380" r="6" fill="none" stroke="var(--brand-red)" stroke-width="4" stroke-dasharray="3 2"/>
    <text class="benefit-label" x="206" y="444">Dedicated Account</text>
    <text class="benefit-label" x="206" y="463">Manager Handles</text>
    <text class="benefit-label" x="206" y="482">everything for you</text>
  </g>
</svg>

</body>
</html>
```